Brindle Works - Fast, Efficient and Gas Mainteance for Domestic, Commercial and Industrial clients

We are in the process of purchasing a new business and would like to get a new logo and business card.
Business is a gas maintenance business that also does new gas installations.
Has been established since 1988.
Services include:
Install all types of gas appliances & equipment inc. hot water units
Maintain / repair / replace all types of gas appliances & equipment

Target Market(s)

Domestic, Commercial and Industrial clients

Industry/Entity Type

Business

Contact Information for Business Card

admin@brindleworks-example.com.au
07 5981 4726
Brindle Works PTY LTD

Logo Text

Gas Fitting & Plumbing Maintenance Specialists

Font styles to use
Sans Serif

Requirements
Must have
• Logo
• Business name, contact number, email address, web address
• Domestic | Commercial | Industrial Est Since 1988
Nice to have
• Possibly a black card with a flame logo to one side
Should not have
• Spelling errors

```html
<!DOCTYPE html>
<html lang="en">
<head>
<meta charset="utf-8">
<title>Brindle Works PTY LTD – Business Card</title>
<link rel="stylesheet" href="https://fonts.googleapis.com/css2?family=Tinos:wght@700&family=Open+Sans:wght@400;600;700&family=Great+Vibes&display=swap">
<style>
  :root {
    --orange: #ef5a3a;
    --charcoal: #393f48;
    --card: #e8e8e8;
    --muted: #5b6068;
    --faint: #d2d2d4;
    --stage: #dcd8d3;
    --white: #ffffff;
  }
  * { margin: 0; padding: 0; box-sizing: border-box; }
  html, body { width: 1189px; height: 1200px; overflow: hidden; }
  body { background: var(--stage); position: relative; font-family: "Open Sans", Arial, sans-serif; }

  .card {
    position: absolute; left: 137px; width: 916px; height: 524px;
    background: var(--card); overflow: hidden;
    box-shadow: 0 4px 10px rgba(0,0,0,0.25);
  }
  .card--front { top: 45px; }
  .card--back { top: 622px; }

  .card__swoosh { position: absolute; inset: 0; width: 100%; height: 100%; }
  .emblem { position: absolute; border-radius: 50%; background: var(--faint); opacity: 0.7; }
  .card--front .emblem { left: 98px; top: 125px; width: 90px; height: 90px; }
  .card--back .emblem { left: 309px; top: 80px; width: 300px; height: 300px; opacity: 0.55; }

  .abs { position: absolute; line-height: 1; white-space: nowrap; }
  .brand { font-family: "Tinos", "Times New Roman", serif; font-weight: 700; color: var(--orange); }
  .legal { font-family: "Open Sans", Arial, sans-serif; font-weight: 700; color: var(--charcoal); }
  .specialty { font-family: "Open Sans", Arial, sans-serif; font-weight: 600; color: var(--charcoal); }

  .card--front .brand { left: 206px; top: 110px; font-size: 52px; }
  .card--front .legal { left: 749px; top: 139px; font-size: 15px; }
  .card--front .specialty { left: 204px; top: 171px; font-size: 35px; }
  .sectors { left: 205px; top: 229px; font-size: 19px; color: var(--muted); }
  .established { left: 541px; top: 222px; font-family: "Great Vibes", cursive; font-size: 32px; color: var(--muted); }

  .contact { font-family: "Tinos", "Times New Roman", serif; font-size: 28px; color: var(--white); }
  .phone { left: 113px; }
  .web { left: 441px; }
  .row-1 { top: 416px; }
  .row-2 { top: 461px; }
  .icon { position: absolute; width: 24px; height: 24px; }
  .divider { position: absolute; left: 361px; top: 414px; width: 3px; height: 74px; background: var(--white); }

  .card--back .brand { left: 125px; top: 206px; font-size: 62px; }
  .card--back .legal { left: 738px; top: 238px; font-size: 15px; }
  .card--back .specialty { left: 123px; top: 274px; font-size: 38px; }
</style>
</head>
<body>

<section class="card card--front" aria-label="Business card front">
  <svg class="card__swoosh" viewBox="0 0 1123 642" preserveAspectRatio="none" aria-hidden="true">
    <path fill="var(--charcoal)" d="M0,110 C110,320 320,440 520,442 C720,444 900,350 985,268 C880,392 720,472 520,472 C300,472 90,360 0,230 Z"/>
    <path fill="var(--orange)" d="M0,245 C130,400 330,486 540,486 C780,486 1000,360 1123,120 L1123,642 L0,642 Z"/>
  </svg>
  <div class="emblem" role="img" aria-label="Faint brand emblem"></div>

  <div class="abs brand">BRINDLE WORKS</div>
  <div class="abs legal">PTY LTD</div>
  <div class="abs specialty">Gas fitting &amp; Plumbing Specialists</div>
  <div class="abs sectors">Domestic | Commercial | Industrial</div>
  <div class="abs established">Est Since 1988</div>

  <div class="abs contact phone row-1">07 5981 4726</div>
  <div class="abs contact phone row-2">07 5981 4739</div>
  <svg class="icon" style="left:308px;top:418px" viewBox="0 0 24 24" aria-label="Phone">
    <rect width="24" height="24" rx="2" fill="var(--white)"/>
    <path fill="var(--orange)" d="M4,9 C4,6 20,6 20,9 L20,11 L16,11 L16,9 L8,9 L8,11 L4,11 Z M7,12 L17,12 L19,19 L5,19 Z"/>
    <circle cx="12" cy="15.5" r="2" fill="var(--white)"/>
  </svg>
  <svg class="icon" style="left:308px;top:463px" viewBox="0 0 24 24" aria-label="Fax">
    <rect width="24" height="24" rx="2" fill="var(--white)"/>
    <rect x="7" y="4" width="10" height="5" fill="var(--orange)"/>
    <rect x="4" y="10" width="16" height="7" fill="var(--orange)"/>
    <rect x="7" y="15" width="10" height="5" fill="var(--orange)" stroke="var(--white)" stroke-width="1"/>
  </svg>
  <div class="divider"></div>
  <svg class="icon" style="left:388px;top:416px" viewBox="0 0 24 24" aria-label="Website">
    <rect width="24" height="24" rx="2" fill="var(--white)"/>
    <circle cx="12" cy="12" r="8" fill="var(--orange)"/>
    <path fill="none" stroke="var(--white)" stroke-width="1.4" d="M12,4 C8,8 8,16 12,20 M12,4 C16,8 16,16 12,20 M4,12 L20,12"/>
  </svg>
  <svg class="icon" style="left:388px;top:461px" viewBox="0 0 24 24" aria-label="Email">
    <rect width="24" height="24" rx="2" fill="var(--white)"/>
    <rect x="4" y="7" width="16" height="11" fill="var(--orange)"/>
    <path fill="none" stroke="var(--white)" stroke-width="1.4" d="M4,7 L12,13 L20,7"/>
  </svg>
  <div class="abs contact web row-1">www.brindleworks-example.com.au</div>
  <div class="abs contact web row-2">admin@brindleworks-example.com.au</div>
</section>

<section class="card card--back" aria-label="Business card back">
  <div class="emblem" role="img" aria-label="Faint brand emblem"></div>
  <div class="abs brand">BRINDLE WORKS</div>
  <div class="abs legal">PTY LTD</div>
  <div class="abs specialty">Gas fitting &amp; Plumbing Specialists</div>
</section>

</body>
</html>
```